Home Inspection Flyer

Looking to have flyer designed that features our business, services, and our contact information. There are three of us. We are all business partners and do not have a company phone number. So each of us would need to be listed on flyer along with our individual phone number. Everything you could possibly need is on our website from logo to services and contact information. https://larkmeadowhomereview.com/. If you could possible incorporate our company colors that would be great. You can find those in our logo top left hand side of website and attached. Please also include our velcorant and brev logos ( home inspector affiliations ) on brochure as well. Those can be found on website. Please feel free to reach out with any questions.
Thanks
Dale
Updates
Looking to get a few tri fold designs. All the ones submitted have been 8x11

```html
<!DOCTYPE html>
<html lang="en">
<head>
<meta charset="utf-8">
<title>Larkmeadow Home Review – Flyer</title>
<link href="https://fonts.googleapis.com/css2?family=Bebas+Neue&family=Montserrat:wght@400;500;600;700;800&display=swap" rel="stylesheet">
<style>
  :root{
    --purple:#8a1ccf;
    --green:#8dc63f;
    --navy:#0e5186;
    --ink:#231f20;
    --body:#3a3a3a;
    --white:#ffffff;
    --backdrop:#dcdcdc;
  }
  *{margin:0;padding:0;box-sizing:border-box;}
  html,body{width:1200px;height:1200px;overflow:hidden;background:var(--backdrop);}
  body{font-family:"Montserrat",sans-serif;position:relative;}
  .flyer{position:absolute;left:190px;top:20px;width:820px;height:1160px;background:var(--white);overflow:hidden;}
  .hero-art{position:absolute;left:0;top:0;width:820px;height:417px;}
  .brand{position:absolute;left:37px;top:96px;display:flex;align-items:center;gap:12px;}
  .brand-mark{width:26px;height:26px;background:var(--green);}
  .brand-name{font-weight:700;color:var(--ink);font-size:25px;line-height:1.08;letter-spacing:.5px;}
  .slogan{position:absolute;left:37px;top:222px;font-family:"Bebas Neue",sans-serif;color:var(--white);font-size:54px;letter-spacing:1px;line-height:64px;white-space:nowrap;}
  .audience{position:absolute;left:37px;top:318px;font-size:18px;line-height:27px;color:var(--ink);}
  .audience b{font-weight:800;}
  .about{position:absolute;left:37px;top:440px;width:725px;}
  .about h2{color:var(--navy);font-weight:800;font-size:24px;letter-spacing:.1px;margin-bottom:12px;}
  .about p{font-size:13.4px;line-height:19.2px;color:var(--body);text-align:justify;font-weight:500;}
  .about p + p{margin-top:19px;}
  .services-head{position:absolute;left:0;top:669px;width:820px;height:85px;background:var(--purple);color:var(--white);text-align:center;}
  .services-head h3{font-size:29px;font-weight:700;margin-top:11px;}
  .services-head p{font-size:18px;font-weight:500;margin-top:2px;letter-spacing:.3px;}
  .services{position:absolute;left:0;top:754px;width:820px;height:158px;background:var(--navy);}
  .service{position:absolute;display:flex;align-items:center;gap:7px;color:var(--white);font-size:16px;line-height:17px;font-weight:500;}
  .service-icon{width:31px;height:31px;background:var(--green);border-radius:3px;display:flex;align-items:center;justify-content:center;flex:none;}
  .badge{position:absolute;width:54px;height:54px;border-radius:50%;}
  .badge.gold{background:#e3b524;border:3px solid #f6d660;}
  .badge.grey{background:#4a4a48;border:3px solid #9a9a94;}
  .region-tab{position:absolute;left:181px;top:912px;width:443px;height:39px;}
  .region-tab span{position:absolute;left:0;top:0;width:100%;line-height:39px;text-align:center;color:var(--white);font-size:17.5px;font-weight:500;}
  .partner{position:absolute;top:970px;}
  .portrait{width:70px;height:70px;border-radius:4px;background:linear-gradient(160deg,#6d6f6a,#2b2c2b 70%);}
  .partner-name{color:var(--green);font-size:14px;font-weight:500;margin-top:5px;}
  .partner-role{color:var(--ink);font-size:10px;font-weight:600;margin-top:2px;}
  .partner-cert{color:var(--ink);font-size:7.6px;font-weight:500;margin-top:1px;}
  .partner-contact{color:var(--purple);font-size:12.4px;font-weight:500;line-height:17px;margin-top:5px;}
  .divider{position:absolute;top:976px;width:1px;height:139px;background:#555;}
  .footer-bar{position:absolute;left:0;top:1146px;width:820px;height:14px;display:flex;}
  .footer-bar .g{flex:1;background:var(--green);}
  .footer-bar .p{flex:1;background:var(--purple);}
</style>
</head>
<body>
<main class="flyer">
  <svg class="hero-art" viewBox="0 0 820 417" width="820" height="417">
    <defs>
      <linearGradient id="heroPhoto" x1="0" y1="0" x2="0" y2="1">
        <stop offset="0" stop-color="#7aa7d8"/>
        <stop offset="0.35" stop-color="#c9c2b8"/>
        <stop offset="0.75" stop-color="#d8d2c8"/>
        <stop offset="1" stop-color="#7a9a52"/>
      </linearGradient>
    </defs>
    <polygon role="img" aria-label="Photo of a two-storey house examined through a magnifying glass held in a hand" points="459,0 820,0 820,417 453,417 357,291 334,217" fill="url(#heroPhoto)"/>
    <polygon points="0,291 357,291 453,417 0,417" fill="var(--green)"/>
    <polygon points="0,217 376,217 332,291 0,291" fill="var(--purple)"/>
  </svg>

  <div class="brand">
    <div class="brand-mark"></div>
    <div class="brand-name">LARKMEADOW<br>HOME REVIEW</div>
  </div>

  <div class="slogan">“THE SEE-2 CREW"</div>

  <p class="audience">For <b>Homeowners, Buyers, Sellers,</b><br><b>FSBOs, Real Estate Agents,</b><br>&amp; <b>Contractors</b></p>

  <section class="about">
    <h2>What Is A Larkmeadow Home Buyer Inspection?</h2>
    <p>A home buyer inspection is a visual examination of a home and its systems: interior plumbing, electrical, roof, attics (temperature permitting), and visible areas of walls, ceilings, floors, foundations, etc. No house is perfect. If an inspector finds a problem it is not an indication the home should not be purchased, nor does an inspection represent a work order for repairs. It simply serves to educate you as to the condition of the home.</p>
    <p>Watch this short video for an easy overview of our home buyer inspection process. Check out this photographic flip-list of the categories covered in the report.</p>
  </section>

  <header class="services-head">
    <h3>Larkmeadow Home Review Services</h3>
    <p>Select An Inspection Or Testing Service For More Information</p>
  </header>

  <section class="services">
    <div class="service" style="left:105px;top:28px;">
      <span class="service-icon"><svg width="20" height="20" viewBox="0 0 20 20"><path d="M10 2 1 10h3v8h4v-5h4v5h4v-8h3z" fill="var(--ink)"/></svg></span>
      <span>Home<br>Inspection</span>
    </div>
    <div class="service" style="left:277px;top:28px;">
      <span class="service-icon"><svg width="20" height="20" viewBox="0 0 20 20" fill="none" stroke="var(--ink)" stroke-width="1.4"><ellipse cx="10" cy="11" rx="3.5" ry="6"/><path d="M6.5 8 3 5M13.5 8 17 5M6.5 12H2M13.5 12H18M7 15l-3 3M13 15l3 3"/></svg></span>
      <span>Pest<br>Inspection</span>
    </div>
    <div class="service" style="left:419px;top:28px;">
      <span class="service-icon"><svg width="20" height="20" viewBox="0 0 20 20" fill="none" stroke="var(--ink)" stroke-width="1.6"><path d="M8 3a2 2 0 0 1 4 0v9a3.5 3.5 0 1 1-4 0z"/><circle cx="10" cy="15" r="1.4" fill="var(--ink)"/></svg></span>
      <span>Radon<br>Inspection</span>
    </div>
    <div class="service" style="left:556px;top:28px;">
      <span class="service-icon"><svg width="20" height="20" viewBox="0 0 20 20"><rect x="2" y="6" width="11" height="9" rx="1" fill="var(--ink)"/><path d="m13 9 5-3v9l-5-3z" fill="var(--ink)"/></svg></span>
      <span>Sewer Camera<br>Inspection</span>
    </div>
    <div class="service" style="left:188px;top:96px;">
      <span class="service-icon"><svg width="20" height="20" viewBox="0 0 20 20" fill="none" stroke="var(--ink)" stroke-width="1.6"><path d="M5 18V6a3 3 0 0 1 6 0M8 8h7"/><path d="M11 11v1M14 11v1M12 14v1M15 14v1M13 17v1" stroke-width="1.3"/></svg></span>
      <span>Water<br>Sample Test</span>
    </div>
    <div class="service" style="left:360px;top:96px;">
      <span class="service-icon"><svg width="20" height="20" viewBox="0 0 20 20" fill="none" stroke="var(--ink)" stroke-width="1.3"><path d="M3 5q2-1.5 3.5 0t3.5 0 3.5 0 3.5 0M3 9q2-1.5 3.5 0t3.5 0 3.5 0 3.5 0M3 13q2-1.5 3.5 0t3.5 0 3.5 0 3.5 0M3 17h14"/></svg></span>
      <span>Well<br>Flow Test</span>
    </div>
    <div class="service" style="left:502px;top:96px;">
      <span class="service-icon"><svg width="20" height="20" viewBox="0 0 20 20" fill="var(--ink)"><circle cx="4" cy="5" r="1.6"/><circle cx="9" cy="5" r="1.6"/><circle cx="14" cy="5" r="1"/><circle cx="17" cy="5" r="1"/><circle cx="4" cy="10" r="1.6"/><circle cx="9" cy="10" r="1"/><circle cx="14" cy="10" r="1"/><circle cx="17" cy="10" r="1"/><circle cx="4" cy="15" r="1"/><circle cx="9" cy="15" r="1"/><circle cx="14" cy="15" r="1"/><circle cx="17" cy="15" r="1"/></svg></span>
      <span>Septic Dye<br>Flow Test</span>
    </div>
    <div class="badge gold" style="left:656px;top:85px;" role="img" aria-label="brev membership seal"></div>
    <div class="badge grey" style="left:720px;top:85px;" role="img" aria-label="velcorant certification seal"></div>
  </section>

  <div class="region-tab">
    <svg width="443" height="39" viewBox="0 0 443 39"><polygon points="0,0 443,0 416,39 26,39" fill="var(--green)"/></svg>
    <span>Pittsburgh's Top-Rated Home Inspectors</span>
  </div>

  <article class="partner" style="left:37px;">
    <div class="portrait" role="img" aria-label="Portrait of Corbin Hale"></div>
    <div class="partner-name">Corbin Hale</div>
    <div class="partner-role">Co-Owner &amp; Principal Partner</div>
    <div class="partner-cert">Certified Home Inspector &amp; Building Consultant</div>
    <div class="partner-contact">(724) 555-0148<br>corbin@larkmeadow.com</div>
  </article>
  <div class="divider" style="left:262px;"></div>
  <article class="partner" style="left:288px;">
    <div class="portrait" role="img" aria-label="Portrait of Wes Tolliver"></div>
    <div class="partner-name">Wes Tolliver</div>
    <div class="partner-role">Co-Owner &amp; Principal Partner</div>
    <div class="partner-cert">Certified Home Inspector &amp; Building Consultant</div>
    <div class="partner-contact">(412) 555-0193<br>wes@larkmeadow.com</div>
  </article>
  <div class="divider" style="left:502px;"></div>
  <article class="partner" style="left:528px;">
    <div class="portrait" role="img" aria-label="Portrait of Dale Renwick"></div>
    <div class="partner-name" style="margin-top:10px;">Dale Renwick</div>
    <div class="partner-role">Certified Home Inspector &amp; Building Consultant</div>
    <div class="partner-contact" style="margin-top:8px;">(412) 555-0167<br>dale@larkmeadow.com</div>
  </article>

  <div class="footer-bar"><div class="g"></div><div class="p"></div></div>
</main>
</body>
</html>
```